Business Card Design Project

I am a psychotherapist, counselor and expressive arts therapist (means I use every art form imaginable in the service of healing). I'm just starting out in private practice in San Francisco, CA. I work with individual adults, children and families. I'd like the card to mirror the simplicity and color palate of my website. I also would love if there is a symbol, image of fire, flame or spark (that is warming, not frightening).

Check out my website: www.lorabeckettmft.com

I want the cards to be printed in letter press so please keep that in mind!

Target Market(s)

Upper Middle Class Adults who are progressively minded, artistic or artists, open to psychotherapy, interested in health & healing.

Industry/Entity Type

Business

Requirements
Must have
• Text to be included:

Lora Beckett
Counseling, Psychotherapy & Expressive Arts

2814 Wexford Avenue, Suite F
San Francisco, CA 94127
p. 415.862.3097
lorajanebeckett@mailvane.net

www.lorabeckettmft.com

MFT License Number 68947

It's OK to abbreviate Number to # or Street to St., etc.

Must be compatible with letter press printing.
Nice to have
• I don't have a logo. I don't expect designers to necessarily create one for me, but if someone comes up with a simple image (see above about flame), that would be great. I don't have much of a budget now, but expect that to change in the next year or so and then could buy a logo for my website, future letterhead, etc.

```html
<!DOCTYPE html>
<html lang="en">
<head>
<meta charset="utf-8">
<title>Lora Beckett – Business Card</title>
<link rel="stylesheet" href="https://fonts.googleapis.com/css2?family=Roboto+Slab:wght@400;700&display=swap">
<style>
  :root {
    --backdrop: #c9c9c7;
    --card-dark: #111111;
    --card-mid: #2e2e2e;
    --ink-light: #ececec;
    --ink-muted: #a3a3a3;
    --rule: #8a8a8a;
    --ember: #d9a521;
    --band: #6f6f6f;
  }
  * { box-sizing: border-box; margin: 0; padding: 0; }
  html, body {
    width: 1200px; height: 1200px; overflow: hidden;
    background: var(--backdrop);
    font-family: "Roboto Slab", Georgia, serif;
  }
  .sheet {
    position: relative; width: 1200px; height: 1200px;
  }
  .card {
    position: absolute; left: 150px; width: 900px; height: 514px;
    background: radial-gradient(ellipse at 55% 0%, var(--card-mid) 0%, #1c1c1c 55%, var(--card-dark) 100%);
    box-shadow: 0 8px 24px rgba(0,0,0,0.25);
    overflow: hidden;
  }
  .card--front { top: 52px; }
  .card--back { top: 634px; }

  /* Front */
  .front-mark {
    position: absolute; left: 190px; top: 202px;
    width: 44px; height: 44px; border-radius: 50%;
    background: var(--ember);
    box-shadow: 0 0 40px rgba(217,165,33,0.45);
  }
  .front-identity {
    position: absolute; left: 262px; top: 196px;
  }
  .front-name {
    font-weight: 700; font-size: 46px; letter-spacing: 2px;
    color: var(--ink-light); text-transform: uppercase; line-height: 1;
  }
  .front-tagline {
    margin-top: 10px; font-size: 22px; color: var(--ink-light); line-height: 1.25;
    width: 420px;
  }

  /* Back */
  .back-name {
    position: absolute; left: 60px; top: 46px;
    font-weight: 700; font-size: 34px; color: var(--ink-light);
  }
  .back-tagline {
    position: absolute; left: 60px; top: 96px;
    font-size: 20px; color: var(--ink-muted);
  }
  .back-license {
    position: absolute; left: 60px; top: 124px;
    font-size: 20px; color: var(--ink-muted);
  }
  .contact-row {
    position: absolute; left: 40px; width: 560px;
    border-bottom: 2px solid var(--rule);
    display: flex; align-items: flex-start; gap: 12px;
    padding-bottom: 6px;
    font-size: 20px; color: var(--ink-muted); line-height: 1.2;
  }
  .contact-row svg { flex: none; margin-top: 2px; }
  .contact-row--address { top: 156px; }
  .contact-row--mail { top: 218px; width: 510px; }
  .contact-row--web { top: 252px; width: 460px; }
  .contact-row--web .contact-text { padding-left: 0; }
  .icon-spacer { width: 26px; flex: none; }

  .band {
    position: absolute; left: 0; top: 386px; width: 900px; height: 10px;
    background: var(--band);
  }
  .band--lower { top: 420px; left: 300px; width: 600px; }
  .phone {
    position: absolute; right: 60px; top: 440px;
    display: flex; align-items: center; gap: 10px;
    font-weight: 700; font-size: 26px; letter-spacing: 1px; color: var(--ink-muted);
  }
</style>
</head>
<body>
<main class="sheet">

  <section class="card card--front" aria-label="Card front">
    <div class="front-mark"></div>
    <div class="front-identity">
      <h1 class="front-name">Lora Beckett</h1>
      <p class="front-tagline">Counseling, Psychotherapy &amp; Expressive Arts</p>
    </div>
  </section>

  <section class="card card--back" aria-label="Card back">
    <h2 class="back-name">Lora Beckett</h2>
    <p class="back-tagline">Counseling, Psychotherapy &amp; Expressive Arts</p>
    <p class="back-license">MFT License Number 68947</p>

    <div class="contact-row contact-row--address">
      <svg width="26" height="24" viewBox="0 0 26 24" aria-hidden="true">
        <path d="M2 12 L13 2 L24 12 M6 10 V22 H20 V10" fill="none" stroke="#a3a3a3" stroke-width="2.5"/>
      </svg>
      <span class="contact-text">2814 Wexford Avenue, Suite F<br>San Francisco, CA 94127</span>
    </div>

    <div class="contact-row contact-row--mail">
      <svg width="26" height="20" viewBox="0 0 26 20" aria-hidden="true">
        <rect x="1.5" y="2" width="23" height="16" fill="none" stroke="#a3a3a3" stroke-width="2"/>
        <path d="M1.5 2 L13 11 L24.5 2" fill="none" stroke="#a3a3a3" stroke-width="2"/>
      </svg>
      <span class="contact-text">lorajanebeckett@mailvane.net</span>
    </div>

    <div class="contact-row contact-row--web">
      <svg width="26" height="22" viewBox="0 0 26 22" aria-hidden="true">
        <path d="M4 1 L4 19 L9 14 L13 21 L16 19.5 L12 12.5 L19 12.5 Z" fill="#a3a3a3"/>
      </svg>
      <span class="contact-text">www.lorabeckettmft.com</span>
    </div>

    <div class="band" role="img" aria-label="Striped decorative band"></div>
    <div class="band band--lower" role="img" aria-label="Striped decorative band"></div>

    <p class="phone">
      <svg width="16" height="26" viewBox="0 0 16 26" aria-hidden="true">
        <rect x="1.5" y="1.5" width="13" height="23" rx="2.5" fill="none" stroke="#a3a3a3" stroke-width="2"/>
        <line x1="6" y1="21" x2="10" y2="21" stroke="#a3a3a3" stroke-width="2"/>
      </svg>
      415 862 3097
    </p>
  </section>

</main>
</body>
</html>
```